Stationary for a Consulting Firm
The Summit Compass Incorporated
Project: Stationary for a Consulting Firm
Stationary for a Consulting Firm - Consulting
Creative Brief
Professional
Dr. Gordon T. Feld
President
47 Maple Crest Okotoks, AB T2Q 4M9
gfeld@summitcompass.ca
www.summitcompass.ca
Business Cards, Stationary, Fax Cover Sheet, and Envelopes are required
Canada's Summit Compass

```html
<!DOCTYPE html>
<html lang="en">
<head>
<meta charset="utf-8">
<title>The Summit Compass Incorporated — Stationery</title>
<link href="https://fonts.googleapis.com/css2?family=Montserrat:wght@700;800&family=Open+Sans:wght@400;600;700&display=swap" rel="stylesheet">
<style>
  :root {
    --bg: #2b2d4a;
    --paper: #ffffff;
    --blue: #1f74bd;
    --blue-deep: #17508f;
    --blue-pale: #eaf2f9;
    --ink: #4a5566;
    --rule: #c9d2dc;
    --shade: rgba(0,0,0,.28);
  }
  * { box-sizing: border-box; margin: 0; padding: 0; }
  html, body { width: 1200px; height: 864px; overflow: hidden; }
  body { background: var(--bg); font-family: "Open Sans", Arial, sans-serif; color: var(--ink); position: relative; }

  .piece { position: absolute; background: var(--paper); box-shadow: 0 6px 18px var(--shade); overflow: hidden; }

  /* shared brand mark */
  .brand { display: flex; align-items: center; gap: 6px; }
  .brand__dot { width: 16px; height: 16px; border-radius: 50%; background: var(--blue); flex: none; }
  .brand__name { font-family: "Montserrat", Arial, sans-serif; font-weight: 800; color: var(--blue); font-size: 10px; line-height: 1.05; letter-spacing: .5px; text-transform: uppercase; }
  .brand--light .brand__dot { background: #fff; }
  .brand--light .brand__name { color: #fff; }

  .watermark { position: absolute; border-radius: 50%; background: var(--blue-pale); }

  /* sheets */
  .sheet { width: 300px; height: 424px; top: 60px; }
  .sheet--fax { left: 70px; }
  .sheet--letter { left: 400px; }
  .sheet__band { position: absolute; top: 0; left: 0; right: 0; height: 14px; background: linear-gradient(90deg, var(--blue-deep), var(--blue)); }
  .sheet__tab { position: absolute; top: 14px; right: 22px; background: var(--paper); padding: 6px 8px; }
  .sheet__watermark { width: 170px; height: 170px; left: 65px; top: 150px; }
  .sheet__footer { position: absolute; left: 18px; right: 18px; bottom: 14px; border-top: 2px solid var(--blue); padding-top: 4px; display: flex; justify-content: space-between; font-size: 5px; color: var(--ink); }

  .fax-table { position: absolute; left: 18px; top: 58px; width: 190px; border-collapse: collapse; font-size: 5.5px; }
  .fax-table td { border: .6px solid var(--ink); height: 11px; padding: 0 3px; }
  .fax-table .label { width: 28px; font-weight: 700; }
  .fax-title { position: absolute; right: 22px; top: 88px; font-family: "Montserrat", Arial, sans-serif; font-weight: 800; font-size: 14px; color: #1d2a3a; }
  .fax-checks { position: absolute; left: 18px; right: 18px; top: 124px; display: flex; justify-content: space-between; font-size: 5.5px; }
  .fax-checks span::before { content: ""; display: inline-block; width: 5px; height: 5px; border: .6px solid var(--ink); margin-right: 2px; vertical-align: -1px; }

  /* envelopes */
  .envelope { width: 500px; height: 250px; top: 540px; }
  .envelope--back { left: 70px; }
  .envelope--front { left: 630px; }
  .envelope__flap { position: absolute; inset: 0; }
  .envelope__seal { position: absolute; left: 50%; top: 58px; transform: translateX(-50%); flex-direction: column; text-align: center; gap: 4px; }
  .envelope__band { position: absolute; top: 0; left: 0; width: 300px; height: 10px; background: linear-gradient(90deg, var(--blue-deep), var(--blue)); }
  .envelope__brand { position: absolute; left: 28px; top: 34px; }
  .envelope__brand .brand__dot { width: 26px; height: 26px; }
  .envelope__brand .brand__name { font-size: 16px; }
  .envelope__return { position: absolute; left: 28px; top: 82px; font-size: 6px; line-height: 1.5; }
  .envelope__watermark { width: 150px; height: 150px; right: 30px; top: 70px; }

  /* business cards */
  .card { width: 320px; height: 183px; left: 800px; border-radius: 8px; }
  .card--front { top: 70px; }
  .card--back { top: 290px; background: linear-gradient(135deg, var(--blue) 0%, var(--blue-deep) 100%); }
  .card__ribbon { position: absolute; top: 18px; right: 0; width: 170px; height: 40px; background: linear-gradient(90deg, var(--blue), var(--blue-deep)); color: #fff; padding: 6px 12px; }
  .card__name { font-weight: 700; font-size: 11px; }
  .card__role { font-size: 7px; opacity: .9; }
  .card__brand { position: absolute; left: 18px; top: 24px; flex-direction: column; align-items: flex-start; }
  .card__brand .brand__dot { width: 30px; height: 30px; }
  .card__brand .brand__name { font-size: 14px; }
  .card__contact { position: absolute; left: 150px; top: 78px; list-style: none; font-size: 7px; line-height: 1.9; }
  .card__contact li { display: flex; align-items: center; gap: 5px; }
  .card__contact svg { width: 8px; height: 8px; fill: var(--blue); }
  .card__bottom { position: absolute; left: 0; right: 0; bottom: 0; height: 8px; background: var(--blue); }
  .card__watermark { width: 200px; height: 200px; left: -40px; top: -50px; background: rgba(255,255,255,.12); }
  .card__back-brand { position: absolute; right: 18px; bottom: 18px; }
  .card__back-brand .brand__name { font-size: 12px; }
</style>
</head>
<body>

<!-- fax cover sheet -->
<section class="piece sheet sheet--fax">
  <div class="sheet__band"></div>
  <div class="sheet__tab brand"><span class="brand__dot"></span><span class="brand__name">Summit<br>Compass</span></div>
  <table class="fax-table">
    <tr><td class="label">To</td><td></td><td class="label">From</td><td></td></tr>
    <tr><td class="label">Fax</td><td></td><td class="label">Pages</td><td></td></tr>
    <tr><td class="label">Phone</td><td></td><td class="label">Date</td><td></td></tr>
    <tr><td class="label">Re</td><td></td><td class="label">CC</td><td></td></tr>
  </table>
  <div class="fax-title">FAX</div>
  <div class="fax-checks"><span>Urgent</span><span>For Review</span><span>Please Comment</span><span>Please Reply</span></div>
  <div class="watermark sheet__watermark"></div>
  <footer class="sheet__footer"><span>47 Maple Crest Okotoks, AB T2Q 4M9</span><span>gfeld@summitcompass.ca</span><span>www.summitcompass.ca</span></footer>
</section>

<!-- letterhead -->
<section class="piece sheet sheet--letter">
  <div class="sheet__band"></div>
  <div class="sheet__tab brand"><span class="brand__dot"></span><span class="brand__name">Summit<br>Compass</span></div>
  <div class="watermark sheet__watermark"></div>
  <footer class="sheet__footer"><span>47 Maple Crest Okotoks, AB T2Q 4M9</span><span>gfeld@summitcompass.ca</span><span>www.summitcompass.ca</span></footer>
</section>

<!-- business card front -->
<section class="piece card card--front">
  <div class="card__ribbon"><div class="card__name">Dr. Gordon T. Feld</div><div class="card__role">President</div></div>
  <div class="card__brand brand"><span class="brand__dot"></span><span class="brand__name">Summit<br>Compass</span></div>
  <ul class="card__contact">
    <li><svg viewBox="0 0 10 10"><path d="M2 0h2l1 3-1.5 1a6 6 0 0 0 2.5 2.5L7 5l3 1v2c0 1-1 2-2 2A8 8 0 0 1 0 2c0-1 1-2 2-2z"/></svg>(403) 555-0148</li>
    <li><svg viewBox="0 0 10 10"><path d="M0 2h10v6H0zM0 2l5 3.5L10 2" stroke="#fff" stroke-width=".8"/></svg>gfeld@summitcompass.ca</li>
    <li><svg viewBox="0 0 10 10"><circle cx="5" cy="5" r="5"/></svg>www.summitcompass.ca</li>
    <li><svg viewBox="0 0 10 10"><path d="M5 0a3.5 3.5 0 0 1 3.5 3.5C8.5 6 5 10 5 10S1.5 6 1.5 3.5A3.5 3.5 0 0 1 5 0z"/></svg>47 Maple Crest Okotoks, AB T2Q 4M9</li>
  </ul>
  <div class="card__bottom"></div>
</section>

<!-- business card back -->
<section class="piece card card--back">
  <div class="watermark card__watermark"></div>
  <div class="card__back-brand brand brand--light"><span class="brand__dot"></span><span class="brand__name">Summit<br>Compass</span></div>
</section>

<!-- envelope back -->
<section class="piece envelope envelope--back">
  <svg class="envelope__flap" viewBox="0 0 500 250" preserveAspectRatio="none">
    <path d="M0 0 L250 140 L500 0" fill="none" stroke="var(--rule)" stroke-width="1.2"/>
    <path d="M0 250 L200 110 M500 250 L300 110" fill="none" stroke="var(--rule)" stroke-width="1"/>
  </svg>
  <div class="envelope__seal brand"><span class="brand__dot"></span><span class="brand__name">Summit Compass</span></div>
</section>

<!-- envelope front -->
<section class="piece envelope envelope--front">
  <div class="envelope__band"></div>
  <div class="envelope__brand brand"><span class="brand__dot"></span><span class="brand__name">Summit<br>Compass</span></div>
  <div class="envelope__return">The Summit Compass Incorporated<br>47 Maple Crest Okotoks, AB T2Q 4M9</div>
  <div class="watermark envelope__watermark"></div>
</section>

</body>
</html>
```